Business logo, card, letter head design needed

we run Beauty & Styling School, also we have a retail shop in Prahran Vic. we ahve logo for our shop which (glomered tavi Cosmetics) but no logo yet for our academy, we hope can do a double side business card, front for the academy / back for the shop which we would like to use black back ground with our white round logo
Target Market(s)
16 - 40 female
Industry/Entity Type
Retail
Contact Information for Business Card
Kestrel Lane Beauty & Styling School (KLBSS)
Glomered Tavi Cosmetics
Dorotea Vranjesic
Director
47 Tallowby Rd. Prahran Vic 3181
E: dorotea@kestrelbeautyschool.com.au
M: 61-487302516
Academy web: www.kestrelbeautyschool.com.au
Shop web: www.glomeredtavi.com
Logo Text
Kestrel Lane Beauty & Styling School
Logo styles of interest
Wordmark Logo
Lettermark Logo
Look and feel

```html
<!DOCTYPE html>
<html lang="en">
<head>
<meta charset="utf-8">
<title>Beauty &amp; Styling School – Business Card</title>
<link rel="stylesheet" href="https://fonts.googleapis.com/css2?family=Anton&display=swap">
<style>
  :root {
    --ink: #070808;
    --signal-red: #ff0000;
    --paper: #ffffff;
    --card-w: 1200px;
    --card-h: 695px;
  }
  html, body {
    margin: 0;
    padding: 0;
    width: var(--card-w);
    height: var(--card-h);
    overflow: hidden;
    background: var(--paper);
  }
  .business-card {
    position: relative;
    width: var(--card-w);
    height: var(--card-h);
    background: var(--paper);
    font-family: "Anton", Impact, sans-serif;
    overflow: hidden;
  }
  .title-band {
    position: absolute;
    left: 0;
    top: 0;
    width: 877px;
    height: 234px;
    background: var(--ink);
  }
  .school-name {
    position: absolute;
    left: 71px;
    top: 88px;
    margin: 0;
    color: var(--paper);
    font-size: 70px;
    font-weight: 400;
    line-height: 1;
    letter-spacing: 0.2px;
    text-transform: uppercase;
    white-space: nowrap;
  }
  .monogram-block {
    position: absolute;
    left: 877px;
    top: 0;
    width: 323px;
    height: 234px;
    background: var(--signal-red);
    display: flex;
    align-items: center;
    justify-content: center;
  }
  .monogram {
    color: var(--paper);
    font-size: 116px;
    line-height: 1;
    letter-spacing: 2px;
    margin-top: -12px;
  }
  .divider-rule {
    position: absolute;
    left: 876px;
    top: 230px;
  }
  .contact-list {
    position: absolute;
    left: 92px;
    top: 0;
    margin: 0;
    padding: 0;
    list-style: none;
    color: var(--ink);
  }
  .contact-item {
    position: absolute;
    left: 0;
    white-space: nowrap;
    line-height: 1;
  }
  .contact-mobile { top: 480px; font-size: 44px; }
  .contact-email  { top: 558px; font-size: 44px; }
  .contact-web    { top: 644px; font-size: 39px; }
</style>
</head>
<body>
  <main class="business-card">
    <header class="title-band">
      <h1 class="school-name">Beauty &amp; Styling School</h1>
    </header>
    <div class="monogram-block">
      <span class="monogram">KLBSS</span>
    </div>
    <svg class="divider-rule" width="6" height="330" viewBox="0 0 6 330" aria-hidden="true">
      <rect x="0" y="0" width="5" height="326" rx="2.5" fill="var(--signal-red)"/>
    </svg>
    <ul class="contact-list">
      <li class="contact-item contact-mobile">M: 61-487302516</li>
      <li class="contact-item contact-email">E: dorotea@kestrelbeautyschool.com</li>
      <li class="contact-item contact-web">Academy web: www.kestrelbeautyschool.com.au</li>
    </ul>
  </main>
</body>
</html>
```